Personal Chef. Private cooking classes. Catering

Need a business card to tell people that I'm available to provide services of, Personal chef/ cooking instructor/ catering, have more than five years experience in the restaurant industry. Culinary and bachelor's degree from Thornbury & Leigh University. I want the card to have my contact information on the back and maybe an inclosed silver pair of cooking tongs through the middle and front of the card.
Chefmarovin@plexmail.net/(604) 718-2247
Background in Mediterranean, French, Italian, & Southern American cuisine.

Target Market(s)

White collar, blue collar and young adults

Industry/Entity Type

Business

Contact Information for Business Card

Tomas Vering Personal Chef (in the front) Chefmarovin@plexmail.net, 604 718-2247 (in the back) Private cooking classes/ catering events specialize in Mediterranean, Italian, French, and Southern American cuisine Mediterranean/ Thornbury & Leigh Culinary degree

Font styles to use
Serif
Script

Colors
000000
ec1f27
fbed22
f4f8fc

Requirements
Must have
• One cooking tong straight down the middle front side of the card from top to bottom. Small yellow chef hat symbol on back right hand corner of card. Preferred main colors, Burgundy red, light olive green, silver
Nice to have
• Preferred main colors, Burgundy red, light olive green, silver
Should not have
• Too Simple and generic

```html
<!DOCTYPE html>
<html lang="en">
<head>
<meta charset="utf-8">
<title>Tomas Vering — Personal Chef</title>
<link rel="stylesheet" href="https://fonts.googleapis.com/css2?family=Cookie&family=Russo+One&family=Open+Sans&family=Quicksand:wght@500&family=Cousine&display=swap">
<style>
  :root {
    --card-red: #ff1329;
    --card-white: #ffffff;
    --star-yellow: #f4f07a;
    --star-edge: #3d3a12;
    --glow: rgba(255, 255, 255, 0.75);
  }
  html, body {
    margin: 0;
    padding: 0;
    overflow: hidden;
    background: var(--card-white);
  }
  .card {
    position: relative;
    width: 1200px;
    height: 640px;
    overflow: hidden;
    background: var(--card-white);
  }
  .card__band {
    position: absolute;
    inset: 0;
    width: 1200px;
    height: 640px;
  }
  .card__band polygon { fill: var(--card-red); }

  .services {
    position: absolute;
    left: 640px;
    top: 10px;
    margin: 0;
    font-family: "Cookie", cursive;
    font-size: 54px;
    line-height: 52px;
    color: var(--card-white);
    -webkit-text-stroke: 0.6px var(--card-white);
  }
  .chef-name {
    position: absolute;
    left: 44px;
    top: 183px;
    margin: 0;
    font-family: "Russo One", sans-serif;
    font-weight: 400;
    font-size: 53px;
    line-height: 1;
    color: var(--card-white);
  }
  .chef-title {
    position: absolute;
    left: 43px;
    top: 240px;
    margin: 0;
    font-family: "Open Sans", sans-serif;
    font-size: 24px;
    line-height: 1;
    color: var(--card-white);
  }
  .credential {
    position: absolute;
    left: 64px;
    top: 404px;
    display: flex;
    align-items: center;
    gap: 4px;
  }
  .credential__stars { width: 122px; height: 40px; }
  .credential__stars polygon {
    fill: var(--star-yellow);
    stroke: var(--star-edge);
    stroke-width: 1.5;
  }
  .glow-text {
    font-family: "Quicksand", sans-serif;
    font-weight: 500;
    color: var(--card-white);
    text-shadow: 0 0 3px var(--glow), 0 0 6px var(--glow);
  }
  .credential__text {
    font-size: 24px;
    line-height: 1;
    padding-top: 4px;
  }
  .specialties {
    position: absolute;
    left: 750px;
    top: 270px;
    margin: 0;
    padding: 0;
    list-style: none;
    font-size: 24px;
    line-height: 34px;
  }
  .contact {
    position: absolute;
    right: 32px;
    top: 571px;
    margin: 0;
    text-align: right;
    font-family: "Cousine", monospace;
    font-size: 22px;
    line-height: 26px;
    color: var(--card-red);
    font-style: normal;
  }
</style>
</head>
<body>
<main class="card">
  <svg class="card__band" viewBox="0 0 1200 640" aria-hidden="true">
    <polygon points="0,0 1034,0 978,452 0,638"/>
  </svg>

  <p class="services">Private cooking classes<br>Catering events</p>

  <h1 class="chef-name">Tomas Vering</h1>
  <p class="chef-title">Personal Chef</p>

  <div class="credential">
    <svg class="credential__stars" viewBox="0 0 122 40" aria-hidden="true">
      <polygon points="20,2 25,15 38,15 27.5,23 31.5,37 20,28.5 8.5,37 12.5,23 2,15 15,15"/>
      <polygon points="61,2 66,15 79,15 68.5,23 72.5,37 61,28.5 49.5,37 53.5,23 43,15 56,15"/>
      <polygon points="102,2 107,15 120,15 109.5,23 113.5,37 102,28.5 90.5,37 94.5,23 84,15 97,15"/>
    </svg>
    <span class="credential__text glow-text">Thornbury &amp; Leigh Culinary Degree</span>
  </div>

  <ul class="specialties glow-text">
    <li>Specialize in;</li>
    <li>Mediterranean</li>
    <li>Italian</li>
    <li>French</li>
    <li>Southern American</li>
    <li>cuisine</li>
  </ul>

  <address class="contact">
    Phone:604 718-2247<br>
    Chefmarovin@plexmail.net
  </address>
</main>
</body>
</html>
```